Tarvin Year 9 Curriculum Model

We need a graphic that communicates all the overlapping elements of our new curriculum. Perhaps it could involve a series of concentric circles moving out from the centre:
1. the "Ideal Learner" profile at the centre with the school's logo behind it (see uploaded file).
2. The words of the "General Capabilities" from the Australian national curriculum in the next circle moving out of centre: "Ethical Understanding" "Literacy" "Numeracy" "Intercultural Awareness" "ICT Capacity" "Critical and Creative Thinking" "Personal and Social Capability"
3. Next circle out has the subjects: "Mathematics" "English" "Languages" "Health and Physical Education" "Technology" "Religious Education" "Humanities" "Arts" "Science"
4. Next Circle out has the title "Community" and then less important, the words "Local" "Regional" "National"
5. Next circle out is simple called "World"
6. Next circle out is simply called "Future"
IF there is a way to make it look not too bad...:Overlaying all the other aspects, floating somewhere, are the 3 significant priorities for the curriculum: Asia, Indigenous Culture and Sustainability

Target Market(s)

Year 9 (15 year old) school students and their parents, as well as teachers and other visitors to the school. It will be used to explain the curriculum and have on the walls as a reminder.

Industry/Entity Type

School

Requirements
Must have
• All of the words in the brief, with a relational dimension for each.

```html
<!DOCTYPE html>
<html lang="en">
<head>
<meta charset="utf-8">
<title>Tarvin Year 9 Curriculum Model</title>
<link rel="stylesheet" href="https://fonts.googleapis.com/css2?family=Marcellus&family=EB+Garamond:wght@400&display=swap">
<style>
  :root {
    --bg-light: #f4fafd;
    --bg-edge: #cfe6f3;
    --ring-outer: #216a8e;
    --ring-middle: #33c48f;
    --ring-inner: #66fdd8;
    --core-white: #ffffff;
    --subjects: #c21fe0;
    --community: #f2900f;
    --world: #d0068e;
    --future: #78db00;
    --capabilities: #3b10e2;
    --learner: #31b1b2;
    --ink-light: #ffffff;
    --font-title: "Marcellus", serif;
    --font-body: "EB Garamond", serif;
  }
  html, body {
    margin: 0;
    padding: 0;
    width: 1200px;
    height: 900px;
    overflow: hidden;
  }
  .canvas {
    position: relative;
    width: 1200px;
    height: 900px;
    background: radial-gradient(ellipse at center, var(--bg-light) 45%, var(--bg-edge) 100%);
  }
  .model {
    position: absolute;
    inset: 0;
    width: 1200px;
    height: 900px;
  }
  .ring-outer { fill: var(--ring-outer); }
  .ring-middle { fill: var(--ring-middle); }
  .ring-inner { fill: var(--ring-inner); }
  .ring-core { fill: var(--core-white); }
  .petal-subjects { fill: var(--subjects); }
  .petal-community { fill: var(--community); }
  .petal-world { fill: var(--world); }
  .petal-future { fill: var(--future); }
  .petal-capabilities { fill: var(--capabilities); }
  .petal-dots {
    fill: none;
    stroke: var(--ink-light);
    stroke-width: 2.4;
    stroke-linecap: round;
    stroke-dasharray: 0 7;
  }
  .learner-disc { fill: var(--learner); }
  .learner-rim { fill: none; stroke: var(--ink-light); stroke-width: 4; }
  .priority {
    font-family: var(--font-title);
    fill: var(--ink-light);
    text-anchor: middle;
  }
  .priority-asia { font-size: 28px; }
  .priority-indigenous { font-size: 34px; }
  .priority-sustainability { font-size: 36px; }
  .petal-title {
    font-family: var(--font-title);
    fill: var(--ink-light);
    text-anchor: middle;
  }
  .petal-list {
    font-family: var(--font-body);
    fill: var(--ink-light);
    text-anchor: middle;
    font-size: 9.5px;
  }
  .learner-title {
    font-family: var(--font-title);
    fill: var(--ink-light);
    text-anchor: middle;
    font-size: 26px;
  }
  .learner-school {
    font-family: var(--font-title);
    fill: var(--ink-light);
    text-anchor: middle;
    font-size: 10px;
  }
</style>
</head>
<body>
<main class="canvas" role="img" aria-label="Soft pale blue background with a faint interlocking circle pattern">
  <svg class="model" viewBox="0 0 1200 900" xmlns="http://www.w3.org/2000/svg" aria-labelledby="model-title">
    <title id="model-title">Tarvin Year 9 Curriculum Model</title>
    <defs>
      <path id="arc-asia" d="M300,450 A300,300 0 1 1 900,450 A300,300 0 1 1 300,450"/>
      <path id="arc-indigenous" d="M257,450 A343,343 0 1 1 943,450 A343,343 0 1 1 257,450"/>
      <path id="arc-sustainability" d="M210,450 A390,390 0 1 1 990,450 A390,390 0 1 1 210,450"/>
    </defs>

    <g class="priority-rings">
      <circle class="ring-outer" cx="600" cy="450" r="425"/>
      <circle class="ring-middle" cx="600" cy="450" r="375"/>
      <circle class="ring-inner" cx="600" cy="450" r="330"/>
      <circle class="ring-core" cx="600" cy="450" r="285"/>

      <text class="priority priority-asia"><textPath href="#arc-asia" startOffset="8.6%">Asia</textPath></text>
      <text class="priority priority-indigenous"><textPath href="#arc-indigenous" startOffset="43.9%">Indigenous Culture</textPath></text>
      <text class="priority priority-sustainability"><textPath href="#arc-sustainability" startOffset="77.8%">Sustainability</textPath></text>
    </g>

    <g class="petal petal-group-subjects">
      <circle class="petal-subjects" cx="580" cy="307" r="97"/>
      <circle class="petal-dots" cx="580" cy="307" r="88" pathLength="100" stroke-dasharray="0 1.1" stroke-dashoffset="0" style="stroke-dasharray:0 1.1 0 1.1"/>
      <text class="petal-list" x="580" y="260">
        <tspan x="580" dy="0">Mathematics</tspan>
        <tspan x="580" dy="10">English</tspan>
        <tspan x="580" dy="10">Languages</tspan>
        <tspan x="580" dy="10">Health and Physical</tspan>
        <tspan x="580" dy="10">Education</tspan>
        <tspan x="580" dy="10">Technology</tspan>
        <tspan x="580" dy="10">Religious Education</tspan>
        <tspan x="580" dy="10">Humanities</tspan>
        <tspan x="580" dy="10">Arts</tspan>
        <tspan x="580" dy="10">Science</tspan>
      </text>
    </g>

    <g class="petal petal-group-community">
      <circle class="petal-community" cx="728" cy="388" r="96"/>
      <circle class="petal-dots" cx="728" cy="388" r="87" stroke-dasharray="0 7 0 7" transform="rotate(20 728 388)"/>
      <text class="petal-title" x="728" y="357" font-size="22" transform="rotate(-8 728 357)">Community</text>
      <text class="petal-list" x="728" y="376">
        <tspan x="728" dy="0">Local</tspan>
        <tspan x="728" dy="11">Regional</tspan>
        <tspan x="728" dy="11">National</tspan>
      </text>
    </g>

    <g class="petal petal-group-world">
      <circle class="petal-world" cx="698" cy="555" r="96"/>
      <circle class="petal-dots" cx="698" cy="555" r="87"/>
      <text class="petal-title" x="698" y="553" font-size="19">World</text>
    </g>

    <g class="petal petal-group-future">
      <circle class="petal-future" cx="530" cy="578" r="97"/>
      <circle class="petal-dots" cx="530" cy="578" r="88"/>
      <text class="petal-title" x="530" y="585" font-size="19">Future</text>
    </g>

    <g class="petal petal-group-capabilities">
      <circle class="petal-capabilities" cx="448" cy="422" r="97"/>
      <circle class="petal-dots" cx="448" cy="422" r="88"/>
      <text class="petal-title" x="450" y="375" font-size="20" transform="rotate(6 450 375)">General</text>
      <text class="petal-title" x="450" y="396" font-size="20">Capabilities</text>
      <text class="petal-list" x="450" y="415">
        <tspan x="450" dy="0">Ethical Understanding</tspan>
        <tspan x="450" dy="10">Literacy</tspan>
        <tspan x="450" dy="10">Numeracy</tspan>
        <tspan x="450" dy="10">Intercultural Awareness</tspan>
        <tspan x="450" dy="10">ICT Capacity</tspan>
        <tspan x="450" dy="10">Critical and Creative Thinking</tspan>
        <tspan x="450" dy="10">Personal and Social Capability</tspan>
      </text>
    </g>

    <g class="learner">
      <circle class="learner-disc" cx="598" cy="438" r="76"/>
      <circle class="learner-rim" cx="598" cy="438" r="68"/>
      <text class="learner-title" x="598" y="418">Ideal</text>
      <text class="learner-school" x="598" y="442" font-size="13">Tarvin</text>
      <text class="learner-school" x="598" y="458">Catholic College</text>
      <text class="learner-title" x="598" y="486">Learner</text>
    </g>
  </svg>
</main>
</body>
</html>
```